Business Card Design

I am a East Coast Florida based company specializing in hauling air conditioning units and Curb adaptors. I would like to see in the design a pickup truck hauling a goose neck trailer and the use of any colors.

Industry/Entity Type

Air Conditioning

Contact Information for Business Card

Pelican Ridge Freight email@ varela4163@mailbrook.com
Dennis (Denny) Varela, Owner. hauling a/c units and curb adapters
Cell 772-555-0147

```html
<!DOCTYPE html>
<html lang="en">
<head>
<meta charset="utf-8">
<title>Pelican Ridge Freight — Business Card</title>
<link rel="stylesheet" href="https://fonts.googleapis.com/css2?family=Montserrat:wght@500;600;700&display=swap">
<style>
  :root {
    --page-bg: #e6e8ec;
    --card-white: #ffffff;
    --navy: #1b3a6b;
    --orange: #ec7a25;
    --ink: #1b3a6b;
    --text-light: #ffffff;
    --rule: rgba(255, 255, 255, 0.55);
  }
  * { box-sizing: border-box; margin: 0; padding: 0; }
  html, body {
    width: 1200px;
    height: 675px;
    overflow: hidden;
    background: var(--page-bg);
    font-family: "Montserrat", sans-serif;
  }
  .canvas {
    width: 1200px;
    height: 675px;
    display: flex;
    align-items: center;
    justify-content: center;
  }
  .card {
    position: relative;
    width: 840px;
    height: 480px;
    background: var(--card-white);
    box-shadow: 0 12px 30px rgba(20, 30, 50, 0.18);
    overflow: hidden;
  }
  .card__brand {
    position: absolute;
    top: 70px;
    left: 0;
    right: 0;
    text-align: center;
  }
  .brand-name {
    display: inline-flex;
    align-items: center;
    gap: 12px;
    font-size: 34px;
    font-weight: 700;
    color: var(--ink);
    letter-spacing: 0.5px;
  }
  .brand-name__mark {
    width: 16px;
    height: 16px;
    background: var(--orange);
  }
  .card__truck {
    position: absolute;
    top: 140px;
    left: 50%;
    width: 210px;
    height: 110px;
    margin-left: -70px;
    border-radius: 8px;
    background: linear-gradient(135deg, #3d5f9a 0%, #1b3a6b 60%, #9aa3b0 100%);
    z-index: 2;
  }
  .card__band {
    position: absolute;
    left: 0;
    right: 0;
    top: 270px;
    height: 166px;
    background: var(--navy);
  }
  .contact-name {
    position: absolute;
    top: 290px;
    left: 0;
    right: 0;
    text-align: center;
    color: var(--text-light);
  }
  .contact-name__full {
    font-size: 24px;
    font-weight: 600;
    letter-spacing: 0.3px;
  }
  .contact-name__rule {
    width: 260px;
    height: 1px;
    margin: 10px auto 10px;
    background: var(--rule);
  }
  .contact-name__title {
    font-size: 16px;
    font-weight: 500;
  }
  .card__strip {
    position: absolute;
    left: 0;
    right: 0;
    bottom: 0;
    height: 44px;
    background: var(--orange);
    display: flex;
    align-items: center;
    justify-content: space-between;
    padding: 0 28px;
    color: var(--text-light);
    font-size: 16px;
    font-weight: 500;
  }
</style>
</head>
<body>
  <main class="canvas">
    <article class="card">
      <header class="card__brand">
        <span class="brand-name"><span class="brand-name__mark"></span>Pelican Ridge Freight</span>
      </header>

      <div class="card__truck" role="img" aria-label="Illustration of a blue semi truck with a flatbed trailer"></div>

      <section class="card__band"></section>

      <div class="contact-name">
        <p class="contact-name__full">Dennis (Denny) Varela</p>
        <div class="contact-name__rule"></div>
        <p class="contact-name__title">Owner</p>
      </div>

      <footer class="card__strip">
        <span class="contact-phone">P: 772-555-0147</span>
        <span class="service-line">Hauling a/c units and curb adapters</span>
      </footer>
    </article>
  </main>
</body>
</html>
```